Website for School Supplies Business

We are rebuilding this website: http://marlowepenhurst.com.au/ and need a new professional design template created. The site will be built on Shopify so it should work on this platform. Also it should be "responsive-ready" so the developer can make it work on many devices.

Marlowe Penhurst (MP) is a very well respected and trusted school supplies business in Australia. It has been around in Australia for over 20 years, and is widely known and trusted by teachers. You can see their product range on the current website.

The current website, including the logo now looks outdated. There is no need to include the current logo on the template design and we want designs that are not so oriented towards kids. Whilst they sell school supplies the users of the website will be teachers. We would prefer an professional friendly look rather than a kidsy style. In terms of colours we suggest bright and light colours should feature - whilst still keeping a professional, elegant look.

Most of their current orders are made by phone / fax. The teachers look at the catalog (they have physical copies at the school) and then place their orders. A lesser number come through the website but that number will increase significantly over the next year or 2. This new website is to take advantage of this trend towards online orders.

Typically the schools are placing orders for multiple items at once. They will often know what they want to order in advance as they have catalogs. It is very important that it is easy to find items on the site (searching by product name or product code) and it must be easy to order multiple items. The current website has a heavy emphasis on the online catalogs. Whilst we still want these available on the site, we want the focus on these reduced.

We expect the category structure to be quite similar to the current site.

We want the homepage to include an area where there blog posts are shown.

Deliverables include:

1. Homepage design
2. Product page design
3. Category page design
4. Info page design (About Us etc.)

We look forward to your designs!
Updates

Target Market(s)

Australian primary school teachers.

Industry/Entity Type

School

Colors

Designer to choose colors to be used in the design.

Requirements
Must have
• Strong search functionality.

```html
<!DOCTYPE html>
<html lang="en">
<head>
<meta charset="utf-8">
<title>Marlowe Penhurst – Bright ideas for your classroom</title>
<link href="https://fonts.googleapis.com/css2?family=Open+Sans:wght@300;400;600;700&display=swap" rel="stylesheet">
<style>
:root{
  --green:#72a444;
  --blue:#3d7fd9;
  --blue-dark:#2c66bd;
  --ink:#3a3a3a;
  --muted:#8a8a8a;
  --red:#e8452f;
  --panel:#f2f2f2;
  --line:#e2e2e2;
  --footer:#dadada;
  --footer-dark:#454545;
  --social:#555555;
  --white:#ffffff;
}
*{box-sizing:border-box;margin:0;padding:0}
html,body{width:938px;height:1200px;overflow:hidden}
body{font-family:'Open Sans',sans-serif;color:var(--ink);background:var(--white);position:relative}
a{color:inherit;text-decoration:none}

.topbar{position:absolute;left:0;top:0;width:938px;height:31px;background:var(--green);color:var(--white);font-size:9px}
.topbar .links{position:absolute;left:94px;top:0;display:flex;height:31px}
.topbar .links a{display:flex;align-items:center;gap:7px;padding:0 15px;border-right:1px solid rgba(0,0,0,.12);height:31px}
.topbar .links a:first-child{padding-left:0}
.topbar .links a:last-child{border-right:0}
.topbar .welcome{position:absolute;right:104px;top:9px}
.topbar .welcome b{font-weight:600}

.brand{position:absolute;left:94px;top:50px}
.brand h1{font-size:24px;font-weight:700;color:#444;line-height:1}
.brand p{font-size:11px;color:#555;margin-top:1px}
.site-search{position:absolute;left:378px;top:55px;width:466px;height:30px;background:#f3f3f3;border:1px solid #dcdcdc;font-size:10px;color:#aaa;padding:8px}
.site-search svg{position:absolute;right:9px;top:8px}

.mainnav{position:absolute;left:94px;top:112px;width:750px;height:34px;background:var(--blue);display:flex;align-items:center;color:var(--white);font-size:12px}
.mainnav .home{width:46px;height:34px;background:var(--blue-dark);display:flex;align-items:center;justify-content:center;margin-right:12px}
.mainnav a{margin-right:23px}

.hero{position:absolute;left:0;top:146px;width:938px;height:316px;
  background:linear-gradient(180deg,rgba(40,50,42,.25),rgba(40,40,36,.35)),
             linear-gradient(90deg,#3f4a42 0%,#6c675c 22%,#8a7b68 40%,#7b7566 55%,#55635a 78%,#4a574f 100%)}
.hero .photo{position:absolute;left:528px;top:18px;width:318px;height:280px;border-radius:40px;
  background:linear-gradient(125deg,rgba(0,0,0,0) 0%,rgba(231,110,140,.55) 30%,rgba(214,52,52,.75) 55%,rgba(235,196,60,.7) 78%,rgba(0,0,0,0) 100%)}
.hero h2{position:absolute;left:94px;top:94px;color:var(--white);font-size:27px;font-weight:700;letter-spacing:.2px}
.hero p{position:absolute;left:94px;top:134px;width:440px;color:var(--white);font-size:14px;line-height:16px;white-space:nowrap}
.hero .cta{position:absolute;left:94px;top:197px;width:110px;height:38px;background:var(--blue);border-radius:3px;color:var(--white);font-size:17px;display:flex;align-items:center;justify-content:center;box-shadow:0 2px 0 #2a5ea8}
.hero .arrow{position:absolute;top:136px;width:44px;height:44px;border-radius:50%;background:rgba(0,0,0,.45);display:flex;align-items:center;justify-content:center}
.hero .dots{position:absolute;left:447px;top:295px;display:flex;gap:10px}
.hero .dots i{width:8px;height:8px;border-radius:50%;background:var(--white);display:block}

.content{position:absolute;left:93px;top:462px;width:752px;height:565px;border-left:1px solid var(--line);border-right:1px solid var(--line)}
.categories{position:absolute;left:102px;top:480px;width:198px;height:505px;background:var(--panel)}
.categories h3{height:36px;background:var(--blue);color:var(--white);font-size:16px;font-weight:400;padding:8px 10px;border-bottom:1px solid #2c66bd}
.categories ul{list-style:none;padding-top:3px}
.categories li{height:27px;display:flex;align-items:center;font-size:9px;color:var(--muted);padding-left:35px;position:relative;border-bottom:1px solid #e8e8e8}
.categories li::before{content:"";position:absolute;left:15px;top:10px;border-left:4px solid #b8b8b8;border-top:3px solid transparent;border-bottom:3px solid transparent}
.categories li.lg{font-size:11px}
.categories .cat-search{position:absolute;left:8px;top:470px;width:182px;height:28px;background:var(--white);border:1px solid #e2e2e2;font-size:9px;color:#aaa;padding:8px}
.categories .cat-search svg{position:absolute;right:8px;top:7px}

.latest h3{position:absolute;left:312px;top:483px;font-size:16px;font-weight:400;color:#444}
.latest .rule{position:absolute;left:312px;top:516px;width:522px;height:1px;background:#555}
.card{position:absolute;width:164px;height:218px;border:1px solid var(--line);background:var(--white)}
.card .img{height:166px}
.card .img.shelf{background:linear-gradient(180deg,#dcdcd8 0%,#e4e1da 35%,#c9b9a0 48%,#a9685a 62%,#6f7e9c 76%,#8a7a66 90%,#5e544b 100%)}
.card .img.toy{background:linear-gradient(180deg,#e7c483 0%,#dba06a 25%,#c98868 45%,#b9797a 65%,#d4584e 82%,#9da7bf 100%)}
.card .img.desks{background:linear-gradient(180deg,#cfded3 0%,#e6ebe6 25%,#ecd57a 48%,#e3c64f 62%,#cdbf95 80%,#a9a48e 100%)}
.card .name{height:25px;border-bottom:1px solid var(--line);font-size:12px;padding:4px 7px;color:#444}
.card .actions{display:flex;justify-content:center;align-items:center;font-size:11px;color:var(--red);height:26px}
.card .actions span{width:1px;height:14px;background:var(--red);margin:0 15px}
.badge{position:absolute;left:7px;top:0;width:38px;height:28px;background:var(--blue-dark);color:var(--white);font-size:10px;text-align:center;padding-top:4px}
.badge::after{content:"";position:absolute;left:0;bottom:-6px;border-left:19px solid transparent;border-right:19px solid transparent;border-top:6px solid var(--blue-dark)}

.footer{position:absolute;left:0;top:1027px;width:938px;height:146px;background:var(--footer)}
.fcol{position:absolute;top:17px}
.fcol h4{font-size:13px;font-weight:400;color:#444;padding-bottom:3px;border-bottom:1px solid #999;display:inline-block}
.fcol ul{list-style:none;margin-top:16px}
.fcol li{font-size:8px;color:#777;height:19.5px;padding-left:12px;position:relative}
.fcol li::before{content:"";position:absolute;left:0;top:2px;width:4px;height:4px;border-right:1px solid #888;border-top:1px solid #888;transform:rotate(45deg)}
.social{display:grid;grid-template-columns:repeat(4,25px);gap:4px;margin-top:17px;margin-left:0}
.social i{width:25px;height:25px;background:var(--social);display:flex;align-items:center;justify-content:center}
.social i::after{content:"";width:9px;height:9px;border-radius:50%;border:1.5px solid var(--white)}
.copyright{position:absolute;left:0;top:1173px;width:938px;height:27px;background:var(--footer-dark);color:#eee;font-size:9px;text-align:center;padding-top:8px}
</style>
</head>
<body>

<div class="topbar">
  <nav class="links">
    <a href="#"><svg width="8" height="7" viewBox="0 0 8 7"><path d="M4 7 0.6 3.4A1.9 1.9 0 0 1 4 1a1.9 1.9 0 0 1 3.4 2.4Z" fill="#fff"/></svg>wish list (0)</a>
    <a href="#"><svg width="8" height="9" viewBox="0 0 8 9"><circle cx="4" cy="2.2" r="2.2" fill="#fff"/><path d="M0 9a4 4 0 0 1 8 0Z" fill="#fff"/></svg>my Account</a>
    <a href="#"><svg width="13" height="10" viewBox="0 0 13 10"><path d="M0 1h2l2 6h7l1.5-5H3" fill="none" stroke="#fff" stroke-width="1.4"/><circle cx="5" cy="9" r="1" fill="#fff"/><circle cx="10" cy="9" r="1" fill="#fff"/></svg>shopping cart</a>
    <a href="#"><svg width="11" height="8" viewBox="0 0 11 8"><rect x=".5" y=".5" width="10" height="7" fill="none" stroke="#fff"/><rect x="1" y="2" width="9" height="1.3" fill="#fff"/></svg>cheak out</a>
  </nav>
  <div class="welcome">Welcome visitor you can <b>Login</b> or <b>Creat an account</b></div>
</div>

<header>
  <div class="brand">
    <h1>Marlowe Penhurst</h1>
    <p>Bright ideas for your classroom</p>
  </div>
  <div class="site-search">You can search for school equipment
    <svg width="12" height="12" viewBox="0 0 12 12"><circle cx="5" cy="5" r="3.8" fill="none" stroke="#999" stroke-width="1.3"/><path d="M8 8l3 3" stroke="#999" stroke-width="1.4"/></svg>
  </div>
  <nav class="mainnav">
    <span class="home"><svg width="20" height="17" viewBox="0 0 20 17"><path d="M10 1 1 9h3v7h4v-5h4v5h4V9h3Z" fill="#fff"/></svg></span>
    <a href="#">About Us</a><a href="#">Contact Us</a><a href="#">Sign In</a><a href="#">Wish List</a><a href="#">Freight Charges</a>
  </nav>
</header>

<section class="hero" role="img" aria-label="Blurred classroom scene with a pupil raising a hand">
  <div class="photo" role="img" aria-label="Stationery arrangement with notebooks, alarm clock and pencil holder"></div>
  <h2>NEW 2014 CATALOGUE</h2>
  <p>Lorem ipsum dolor sit amet, consectetur adipisicing elit, sed do<br>eiusmod tempor incididunt ut labore et dolore magna aliqua.<br>Ut enim ad minim veniam</p>
  <a class="cta" href="#">Order Now</a>
  <span class="arrow" style="left:24px"><svg width="12" height="20" viewBox="0 0 12 20"><path d="M10 1 1 10l9 9" fill="none" stroke="#fff" stroke-width="1.6"/></svg></span>
  <span class="arrow" style="left:870px"><svg width="12" height="20" viewBox="0 0 12 20"><path d="M2 1l9 9-9 9" fill="none" stroke="#fff" stroke-width="1.6"/></svg></span>
  <div class="dots"><i></i><i></i><i></i></div>
</section>

<div class="content"></div>

<aside class="categories">
  <h3>CATEGORIES</h3>
  <ul>
    <li>New Products for 2014</li><li>Classroom Essentials</li><li>Special Education Resources</li>
    <li>Early Learning Resources</li><li>Language Resources</li><li>Maths Resources</li>
    <li>Science Resources</li><li>Construction Resources</li><li>Art &amp; Craft Resources</li>
    <li>Music Resources</li><li>Puzzles</li><li>Puppets and Animal Character</li>
    <li class="lg">Book Storage and Display</li><li class="lg">Library Resources</li><li>Whiteboard Accessories</li>
  </ul>
  <div class="cat-search">search Categories
    <svg width="12" height="12" viewBox="0 0 12 12"><circle cx="5" cy="5" r="3.8" fill="none" stroke="#bbb" stroke-width="1.3"/><path d="M8 8l3 3" stroke="#bbb" stroke-width="1.4"/></svg>
  </div>
</aside>

<section class="latest">
  <h3>LATEST PRODUCT 2014</h3>
  <div class="rule"></div>

  <article class="card" style="left:319px;top:534px"><div class="img shelf" role="img" aria-label="White book shelf with books and toys"></div><span class="badge">New</span><div class="name">Book storage &amp; display</div><div class="actions">View all<span></span>Add to cart</div></article>
  <article class="card" style="left:495px;top:534px"><div class="img toy" role="img" aria-label="Toddler playing with a colourful toy"></div><div class="name">Child Toy</div><div class="actions">View all<span></span>Add to cart</div></article>
  <article class="card" style="left:670px;top:534px"><div class="img desks" role="img" aria-label="Classroom with yellow desks"></div><div class="name">Classroom Essentials</div><div class="actions">View all<span></span>Add to cart</div></article>

  <article class="card" style="left:319px;top:767px"><div class="img shelf" role="img" aria-label="White book shelf with books and toys"></div><div class="name">Book storage &amp; display</div><div class="actions">View all<span></span>Add to cart</div></article>
  <article class="card" style="left:495px;top:767px"><div class="img toy" role="img" aria-label="Toddler playing with a colourful toy"></div><div class="name">Child Toy</div><div class="actions">View all<span></span>Add to cart</div></article>
  <article class="card" style="left:670px;top:767px"><div class="img desks" role="img" aria-label="Classroom with yellow desks"></div><div class="name">Classroom Essentials</div><div class="actions">View all<span></span>Add to cart</div></article>
</section>

<footer class="footer">
  <div class="fcol" style="left:94px"><h4>INFORMATION</h4><ul><li>About</li><li>Delivery information</li><li>Privacy policy</li><li>Trems &amp; conditions</li></ul></div>
  <div class="fcol" style="left:245px"><h4>CUSTOMERS</h4><ul><li>Contact Us</li><li>Returne</li><li>Site Map</li></ul></div>
  <div class="fcol" style="left:390px"><h4>CONTACT US</h4><ul><li>Location</li><li>Email address</li><li>Phone number</li></ul></div>
  <div class="fcol" style="left:540px"><h4>FOLLOW ON SOCIAL MEDIA</h4><div class="social" aria-label="Social media links"><i></i><i></i><i></i><i></i><i></i><i></i><i></i><i></i></div></div>
  <div class="fcol" style="left:762px"><h4>MY ACCOUNT</h4><ul><li>My account</li><li>Order histry</li><li>Wish list</li><li>New's letter</li></ul></div>
</footer>
<div class="copyright">Copyright 2014 Marlowe Penhurst - All Rights Reserved - Disclaimer - Terms and Conditions - Privacy Policy</div>

</body>
</html>
```